Quiet Iron Hours - Cover for a book exploring how modern men think and feel

The book explores what men in today's world think and feel, and what they want from society and the people in their lives. The idea is to put the focus on men and how they're dealing with a world in which patriarchy is rightly under scrutiny and women are finding and using their voice. How do men feel in the company of more empowered women? What do men want from the women in their lives (not talking about sex here)? Why are men more likely to take their own lives, not coping well with mental health issues?

Target Market(s)

Men and Women

Font styles to use
Other font styles liked:
• Clean and non-fussy font

Colors

Designer to choose colors to be used in the design.

Requirements
Must have
• A silhouette of a man or multiple men from diverse backgrounds and age groups
Nice to have
• The image must be bold and yet understated in its simplicity.
Should not have
• Nothing sexual or suggestive.

```html
<!DOCTYPE html>
<html lang="en">
<head>
<meta charset="utf-8">
<title>Quiet Iron Hours – Book Cover</title>
<link rel="stylesheet" href="https://fonts.googleapis.com/css2?family=Anton&family=Arimo:wght@400&family=Oswald:wght@600&display=swap">
<style>
  :root {
    --backdrop: #6e6a65;
    --cover-orange: #e8573a;
    --cover-orange-light: #ea6a48;
    --cover-black: #050505;
    --ink-black: #111111;
    --paper-white: #ffffff;
    --figure-tone: #3a3a3a;
    --figure-tone-dark: #1c1c1c;
  }
  html, body {
    margin: 0;
    padding: 0;
    width: 1200px;
    height: 939px;
    overflow: hidden;
    background: var(--backdrop);
  }
  .stage {
    position: relative;
    width: 1200px;
    height: 939px;
    display: flex;
    align-items: center;
    justify-content: center;
  }
  .book-cover {
    width: 574px;
    height: 860px;
    display: block;
    box-shadow: 0 18px 40px rgba(0,0,0,0.35);
  }
  .subtitle {
    font-family: "Arimo", Arial, sans-serif;
    font-size: 27px;
    fill: var(--ink-black);
  }
  .title-top {
    font-family: "Anton", "Oswald", sans-serif;
    font-size: 132px;
    fill: var(--ink-black);
  }
  .title-bottom {
    font-family: "Anton", "Oswald", sans-serif;
    font-size: 236px;
    fill: var(--paper-white);
  }
  .author {
    font-family: "Oswald", sans-serif;
    font-weight: 600;
    font-size: 42px;
    letter-spacing: 2px;
    fill: var(--paper-white);
  }
</style>
</head>
<body>
  <main class="stage">
    <svg class="book-cover" viewBox="0 0 574 860" xmlns="http://www.w3.org/2000/svg" aria-label="Book cover: Quiet Iron Hours by Meera Talwar">
      <defs>
        <linearGradient id="orangeBand" x1="0" y1="0" x2="1" y2="1">
          <stop offset="0" stop-color="var(--cover-orange-light)"/>
          <stop offset="1" stop-color="var(--cover-orange)"/>
        </linearGradient>
        <linearGradient id="figureTone" x1="0" y1="0" x2="0" y2="1">
          <stop offset="0" stop-color="var(--figure-tone)"/>
          <stop offset="1" stop-color="var(--figure-tone-dark)"/>
        </linearGradient>
      </defs>

      <rect class="cover-top" x="0" y="0" width="574" height="362" fill="url(#orangeBand)"/>
      <rect class="cover-bottom" x="0" y="362" width="574" height="498" fill="var(--cover-black)"/>

      <text class="subtitle" x="287" y="78" text-anchor="middle">Insights Into How Men &amp;</text>
      <text class="subtitle" x="287" y="114" text-anchor="middle">Women Can Live In Harmony</text>

      <text class="title-top" x="42" y="360" textLength="490" lengthAdjust="spacingAndGlyphs">QUIET IRON</text>
      <text class="title-bottom" x="36" y="600" textLength="500" lengthAdjust="spacingAndGlyphs">HOURS</text>

      <rect class="figure-silhouette" role="img" aria-label="Silhouette of a man walking forward" x="150" y="420" width="44" height="160" rx="6" fill="url(#figureTone)"/>

      <text class="author" x="287" y="790" text-anchor="middle">MEERA TALWAR</text>
    </svg>
  </main>
</body>
</html>
```